Harvesting Victors 6x9 book soft cover- front cover only

We need a book cover for a softcover book. We will need final files in Photoshop or InDesign is preferred.

Overall Title:
Harvesting Victors
Subtitle:
The Foundations of Humble Mentoring for Trainers, Instructors and Players
Author:
by Dr. Marcus Pettiford

The audience is high school and college coaches however we don't want the standard picture with words over the top. Make it a creative design but keep it mind it's a little academic.

```html
<!DOCTYPE html>
<html lang="en">
<head>
<meta charset="utf-8">
<title>Harvesting Victors – Front Cover</title>
<link rel="stylesheet" href="https://fonts.googleapis.com/css2?family=Barlow+Semi+Condensed:wght@500&family=Barlow:wght@400;500&display=swap">
<style>
  :root {
    --page-bg: #f2f3f5;
    --cover-white: #f7fafc;
    --ink-navy: #14264a;
    --band-navy: #2a4a73;
    --band-text: #ffffff;
    --smoke-blue: #2c9bf0;
    --smoke-pale: #cfe7fb;
  }
  * { margin: 0; padding: 0; box-sizing: border-box; }
  html, body {
    width: 1200px;
    height: 850px;
    overflow: hidden;
    background: var(--page-bg);
  }
  .canvas {
    position: relative;
    width: 1200px;
    height: 850px;
  }
  .cover {
    position: absolute;
    left: 340px;
    top: 35px;
    width: 520px;
    height: 780px;
    background: var(--cover-white);
    overflow: hidden;
    box-shadow: 0 6px 24px rgba(20, 38, 74, 0.15);
  }
  .cover-artwork {
    position: absolute;
    inset: 0 0 140px 0;
    width: 100%;
    height: 640px;
  }
  .title-block {
    position: absolute;
    right: 44px;
    top: 108px;
    text-align: right;
    color: var(--ink-navy);
  }
  .book-title {
    font-family: "Barlow Semi Condensed", "Arial Narrow", sans-serif;
    font-weight: 500;
    font-size: 66px;
    line-height: 1.02;
    letter-spacing: 2px;
    text-transform: uppercase;
  }
  .book-subtitle {
    margin-top: 18px;
    margin-left: auto;
    max-width: 290px;
    font-family: "Barlow", sans-serif;
    font-weight: 500;
    font-size: 17px;
    line-height: 1.3;
    letter-spacing: 0.3px;
  }
  .author-band {
    position: absolute;
    left: 0;
    bottom: 0;
    width: 100%;
    height: 140px;
    background: var(--band-navy);
    display: flex;
    align-items: center;
    justify-content: center;
    padding-top: 40px;
  }
  .author-name {
    font-family: "Barlow", sans-serif;
    font-weight: 500;
    font-size: 19px;
    letter-spacing: 1px;
    color: var(--band-text);
  }
</style>
</head>
<body>
<main class="canvas">
  <section class="cover">
    <svg class="cover-artwork" role="img" aria-label="Flowing blue smoke artwork sweeping across the cover from top left to lower right" viewBox="0 0 520 640" preserveAspectRatio="none">
      <defs>
        <radialGradient id="smoke-left" cx="0.15" cy="0.45" r="0.6">
          <stop offset="0" stop-color="var(--smoke-blue)" stop-opacity="0.55"/>
          <stop offset="1" stop-color="var(--smoke-pale)" stop-opacity="0"/>
        </radialGradient>
        <radialGradient id="smoke-lower" cx="0.65" cy="0.85" r="0.55">
          <stop offset="0" stop-color="var(--smoke-blue)" stop-opacity="0.4"/>
          <stop offset="1" stop-color="var(--smoke-pale)" stop-opacity="0"/>
        </radialGradient>
      </defs>
      <rect width="520" height="640" fill="url(#smoke-left)"/>
      <rect width="520" height="640" fill="url(#smoke-lower)"/>
    </svg>

    <header class="title-block">
      <h1 class="book-title">Harvesting<br>Victors</h1>
      <p class="book-subtitle">The Foundations of Humble Mentoring for Trainers, Instructors and Players</p>
    </header>

    <footer class="author-band">
      <p class="author-name">Dr. Marcus Pettiford</p>
    </footer>
  </section>
</main>
</body>
</html>
```